Kellwood Build, Carpentry Services

Business card for carpentry business in the Sunshine Coast.

Business card layout required using logo provided - provided both PDF copy and AI. Please let me know if you would like a the files for the logo symbol and text by itself.

Business Colours are grey, blue and white. The font colours codes for this design are Blue Hex # 00B4E6 and Hex # 39393B for the gray colour.

FYI font for logo is Gotham Bold.

Preference for a clean and striking layout that is simple and elegant.

Target Market(s)

Young Families, retirees, young couples requiring assistance with small to medium works/renovations on the Sunshine Coast.

Industry/Entity Type

Construction

Contact Information for Business Card

Dean Kellwood
Carpenter
0489305627
dean@kellwoodbuild.com.au
Pelican Bay, Coral Coast
RHPA Licensed Carpenter (In smaller font)

Font styles to use
Sans Serif

Colors

Designer to choose colors to be used in the design.

Requirements
Must have
• Logo provided must appear on the card, preferably on one side of the card by itself with the text on the alternate side
Nice to have
• Text on the other side of card, maybe grey background and white font here but happy for the designer to provide ideas here.
Should not have
• Use of other colours, other than the ones provided - white, grey and blue. Black optional.

```html
<!DOCTYPE html>
<html lang="en">
<head>
<meta charset="utf-8">
<title>Kellwood Build – Business Card</title>
<link rel="stylesheet" href="https://fonts.googleapis.com/css2?family=Open+Sans:wght@400;600;700&display=swap">
<style>
  :root {
    --blue: #00B4E6;
    --grey: #39393B;
    --ink: #2a2a2c;
    --white: #ffffff;
    --stage: #1e1e1f;
    --pattern: #2c2c2e;
  }
  * { box-sizing: border-box; margin: 0; padding: 0; }
  html, body {
    width: 1200px; height: 1021px; overflow: hidden;
    background: var(--stage);
    font-family: "Open Sans", sans-serif;
  }
  .card {
    position: absolute; left: 300px;
    width: 600px; height: 343px;
    border-radius: 3px;
    overflow: hidden;
    box-shadow: 0 12px 30px rgba(0,0,0,.45);
  }
  /* back side */
  .card-back { top: 140px; background: var(--grey); }
  .card-back .pattern-field {
    position: absolute; inset: 0;
    background: linear-gradient(135deg, #4a4a4d 0%, var(--pattern) 55%, #232325 100%);
  }
  .card-back .back-mark {
    position: absolute; right: 60px; bottom: 44px;
    display: flex; align-items: center; gap: 8px;
    color: var(--blue); font-weight: 700; font-size: 14px; letter-spacing: .5px;
  }
  .mark-square { width: 12px; height: 12px; background: var(--blue); }

  /* front side */
  .card-front { top: 550px; background: var(--white); color: var(--ink); }
  .brand {
    position: absolute; top: 56px; left: 0; right: 0;
    display: flex; justify-content: center; align-items: center; gap: 14px;
  }
  .brand .mark-square { width: 26px; height: 26px; }
  .brand-name {
    color: var(--blue); font-weight: 700; font-size: 34px;
    letter-spacing: 1px; text-transform: uppercase; line-height: 1.2;
  }
  .brand-tagline {
    position: absolute; top: 112px; left: 0; right: 0; text-align: center;
    color: var(--grey); font-size: 9px; letter-spacing: 4px; text-transform: uppercase;
  }
  .person {
    position: absolute; top: 170px; left: 30px; width: 240px; text-align: right;
  }
  .person-name { color: var(--blue); font-weight: 700; font-size: 20px; text-transform: uppercase; line-height: 1.2; }
  .person-title { color: var(--ink); font-size: 15px; text-transform: uppercase; line-height: 1.3; }
  .divider {
    position: absolute; left: 290px; top: 166px; width: 1px; height: 88px; background: var(--ink);
  }
  .contact {
    position: absolute; top: 168px; left: 310px;
    list-style: none; font-size: 14px; line-height: 21px; color: var(--ink);
  }
  .contact li { display: flex; align-items: center; gap: 7px; white-space: nowrap; }
  .contact .address { font-size: 15px; margin-bottom: 2px; }
  .contact svg { width: 13px; height: 13px; flex: none; fill: none; stroke: var(--blue); stroke-width: 1.6; }
  .licence {
    position: absolute; left: 40px; right: 40px; top: 286px;
    display: flex; align-items: center; gap: 10px;
    font-size: 14px; color: var(--ink); white-space: nowrap;
  }
  .licence::before, .licence::after { content: ""; flex: 1; height: 1px; background: var(--ink); }
</style>
</head>
<body>

<section class="card card-back">
  <div class="pattern-field" role="img" aria-label="Embossed repeating brand-symbol pattern in dark grey tones"></div>
  <div class="back-mark"><span class="mark-square"></span>Kellwood Build</div>
</section>

<section class="card card-front">
  <div class="brand"><span class="mark-square"></span><span class="brand-name">Kellwood Build</span></div>
  <p class="brand-tagline">Carpentry Services</p>

  <div class="person">
    <p class="person-name">Dean Kellwood</p>
    <p class="person-title">Carpenter</p>
  </div>
  <div class="divider"></div>

  <ul class="contact">
    <li class="address">Pelican Bay, Coral Coast</li>
    <li>
      <svg viewBox="0 0 16 16"><path d="M4 1.5l2.5 3-1.5 2a9 9 0 0 0 4.5 4.5l2-1.5 3 2.5-1.5 2.5C7 14 2 9 1.5 3z"/></svg>
      0489305627
    </li>
    <li>
      <svg viewBox="0 0 16 16"><rect x="1.5" y="3.5" width="13" height="9"/><path d="M1.5 3.5L8 9l6.5-5.5"/></svg>
      dean@kellwoodbuild.com.au
    </li>
    <li>
      <svg viewBox="0 0 16 16"><circle cx="8" cy="8" r="6.5"/><path d="M1.5 8h13M8 1.5c3 3.5 3 9.5 0 13M8 1.5c-3 3.5-3 9.5 0 13"/></svg>
      www.kellwoodbuild.com.au
    </li>
  </ul>

  <p class="licence">RHPA Licensed Carpenter</p>
</section>

</body>
</html>
```